Machine shop needs a brochure designed

Would like a tri-fold professional looking brochure that tells about our business and our capabilities. We are a family-owned business with over 50 years of experience in precision manufacturing. We specialize in close-tolerance tooling and serve a diverse array of industries. Our colors are red, black, white, and gray. The final design should make a great impression and spotlight our capabilities and quality.

Target Market(s)

Manufacturing industries needing tooling

Industry/Entity Type

Machining, grinding, manufacturing

Font styles to use
Serif

Colors
EB3D1F
EC4F4E
F09395
F8D3D4
FCEDEE

Requirements
Must have
• Logo, colors are red, black, white, gray
Nice to have
• Images of CNC process or machining/grinding metal parts.

```html
<!DOCTYPE html>
<html lang="en">
<head>
<meta charset="utf-8">
<title>Corvane Industries – Tri-fold Brochure</title>
<link href="https://fonts.googleapis.com/css2?family=Bebas+Neue&family=Montserrat:wght@400;600;700&display=swap" rel="stylesheet">
<style>
  :root{
    --navy:#2a2c40;
    --red:#e31e24;
    --light:#eff0f2;
    --white:#ffffff;
    --page:#e9eaec;
    --ink:#23252f;
  }
  *{box-sizing:border-box;margin:0;padding:0}
  html,body{width:849px;height:1200px;overflow:hidden;background:var(--page)}
  .canvas{position:relative;width:849px;height:1200px;background:var(--page);font-family:"Montserrat",sans-serif;color:var(--ink)}
  .spread{position:absolute;left:105px;width:640px;height:456px;overflow:hidden;background:var(--light)}
  .spread--outside{top:86px}
  .spread--inside{top:651px}
  .spread svg.art{position:absolute;left:0;top:0;width:640px;height:456px}
  .block{position:absolute}
  .headline{font-family:"Bebas Neue","Oswald",sans-serif;font-weight:400;text-transform:uppercase;line-height:1;white-space:nowrap}
  .body-copy{font-size:7.4px;line-height:11.6px}
  .on-dark{color:var(--white)}
  .red{color:var(--red)}

  /* outside spread */
  .intro-title{left:23px;top:78px;font-size:20px;color:var(--white)}
  .intro-copy{left:23px;top:104px;width:178px;font-size:7.6px;line-height:12.7px}
  .contact-title{left:212px;top:333px;width:212px;text-align:center;font-size:19px}
  .contact-list{left:212px;top:355px;width:212px;text-align:center;font-size:8px;line-height:13.4px;color:var(--ink)}
  .contact-list svg{width:6px;height:6px;vertical-align:-0.5px;margin-right:2px}
  .cover-welcome{left:424px;top:331px;width:216px;text-align:center}
  .cover-welcome .w1{display:block;font-size:45px;color:var(--navy)}
  .cover-welcome .w2{display:block;font-size:45px;color:var(--red);margin-top:-6px}
  .cover-tag{display:inline-block;margin-top:-2px;background:var(--navy);color:var(--white);font-family:"Montserrat",sans-serif;font-size:9.6px;font-weight:600;padding:1px 6px;border-radius:2px;letter-spacing:.2px}

  /* inside spread */
  .welcome-title{left:23px;top:77px;font-size:26px;color:var(--navy)}
  .welcome-sub{left:23px;top:102px;font-size:17px;color:var(--red)}
  .welcome-copy{left:23px;top:121px;width:180px}
  .about-title{left:23px;top:221px;font-size:18.5px;color:var(--red)}
  .about-title span{color:var(--navy)}
  .about-copy{left:23px;top:239px;width:180px}
  .about-copy p+p{margin-top:11.6px}
  .letter{left:232px;top:191px;width:186px;font-size:7.3px;line-height:12.3px;white-space:nowrap}
  .letter .greet{display:block;width:120px;text-align:center;font-weight:700}
  .letter .greet span{font-weight:400}
  .signoff{left:232px;top:338px;width:178px;font-size:7.6px;line-height:12px}
  .signoff .regards{font-weight:700;color:var(--navy)}
  .signoff .row{display:flex;justify-content:space-between;color:var(--red);font-weight:700}
  .closing{left:232px;top:386px;width:170px}
  .services-intro{left:443px;top:21px;width:185px;color:var(--white)}
  .cap-label{left:441px;top:47px;background:var(--red);color:var(--white);font-weight:700;font-size:8.2px;padding:2px 4px;letter-spacing:.1px}
  .cap-list{left:443px;top:69px;width:185px;color:var(--white);font-size:7.4px;line-height:11.8px;list-style:none}
  .cap-list li{position:relative;padding-left:7px}
  .cap-list li::before{content:"";position:absolute;left:0;top:4.5px;width:2.6px;height:2.6px;border-radius:50%;background:var(--red)}
  .cap-list .pair{display:flex}
  .cap-list .pair span{width:101px;position:relative}
  .cap-list .pair span+span{padding-left:7px}
  .cap-list .pair span+span::before{content:"";position:absolute;left:0;top:4.5px;width:2.6px;height:2.6px;border-radius:50%;background:var(--red)}
</style>
</head>
<body>
<div class="canvas">

  <!-- OUTSIDE SPREAD -->
  <section class="spread spread--outside">
    <svg class="art" viewBox="0 0 640 456" xmlns="http://www.w3.org/2000/svg">
      <defs>
        <linearGradient id="sparkFill" x1="0" y1="0" x2="1" y2="1">
          <stop offset="0" stop-color="#5b6fb8"/><stop offset=".55" stop-color="#3a3f86"/><stop offset="1" stop-color="#f3a323"/>
        </linearGradient>
        <linearGradient id="drillFill" x1="0" y1="0" x2="0" y2="1">
          <stop offset="0" stop-color="#8d8f94"/><stop offset=".5" stop-color="#4a4b4f"/><stop offset="1" stop-color="#2a2b2e"/>
        </linearGradient>
        <linearGradient id="millFill" x1="0" y1="0" x2="1" y2="1">
          <stop offset="0" stop-color="#1d3550"/><stop offset=".6" stop-color="#3f6a8c"/><stop offset="1" stop-color="#9fb6c8"/>
        </linearGradient>
        <linearGradient id="paperFade" x1="0" y1="0" x2="1" y2="0">
          <stop offset="0" stop-color="#dcdde1"/><stop offset=".15" stop-color="#f4f5f7"/><stop offset="1" stop-color="#eceef0"/>
        </linearGradient>
      </defs>
      <rect x="212" y="0" width="212" height="456" fill="url(#paperFade)"/>
      <rect x="424" y="0" width="216" height="456" fill="url(#paperFade)"/>
      <rect x="0" y="0" width="212" height="456" fill="var(--navy)"/>
      <polygon points="212,0 424,0 424,120 212,230" fill="var(--navy)"/>
      <polygon points="424,0 640,0 640,150 424,60" fill="var(--navy)"/>

      <polygon points="0,0 140,0 0,76" fill="var(--red)"/>
      <polygon points="0,350 30,332 30,456 0,456" fill="var(--white)"/>
      <polygon points="23,228 23,300 82,266" fill="var(--red)"/>
      <polygon points="24,304 205,197 205,456 24,456" fill="var(--white)"/>
      <g role="img" aria-label="Photo: angle grinder throwing sparks on a metal part">
        <polygon points="30,308 199,209 199,456 30,456" fill="url(#sparkFill)"/>
      </g>

      <polygon points="228,125 410,28 410,262 345,300 228,345" fill="var(--white)"/>
      <polygon points="228,63 228,127 285,96" fill="var(--red)"/>
      <g role="img" aria-label="Photo: multi-spindle drilling machine cutting a steel part">
        <polygon points="235,124 400,38 400,252 345,290 235,343" fill="url(#drillFill)"/>
      </g>
      <polygon points="346,289 406,255 406,322" fill="var(--navy)"/>

      <polygon points="521,0 640,0 640,67" fill="var(--red)"/>
      <polygon points="439,28 620,132 620,350 439,250" fill="var(--white)"/>
      <g role="img" aria-label="Photo: CNC milling spindle machining an aluminium block">
        <polygon points="445,38 611,132 611,343 503,285 445,253" fill="url(#millFill)"/>
      </g>
      <polygon points="561,93 618,63 618,127" fill="var(--red)"/>
      <polygon points="439,253 439,321 498,287" fill="var(--navy)"/>
    </svg>

    <h1 class="block headline intro-title">Corvane Industries, Inc.</h1>
    <p class="block body-copy on-dark intro-copy">is committed to quality and consistency. We are constantly striving to implement new ways to adhere to a high mark while providing our clients with their orders in as short a time frame as possible. It is not only our goal, but we understand it to be our responsibility to provide our clients with the highest quality products.</p>

    <h2 class="block headline red contact-title">Corvane Industries,</h2>
    <div class="block contact-list">
      <div><svg viewBox="0 0 10 10"><path d="M2 1l2 2-1 1.5c.7 1.3 1.2 1.8 2.5 2.5L7 6l2 2-1.5 1.5C4.5 9 1 5.5.5 2.5z" fill="var(--red)"/></svg>| 555.014.2230</div>
      <div><svg viewBox="0 0 10 10"><rect x="2.5" y="0.5" width="5" height="3" fill="var(--red)"/><rect x="0.5" y="3.5" width="9" height="4" rx="1" fill="var(--red)"/><rect x="2.5" y="6.5" width="5" height="3" fill="var(--red)"/></svg>| 555.014.2231</div>
      <div><svg viewBox="0 0 10 10"><rect x="0.5" y="2" width="9" height="6.5" fill="var(--red)"/><path d="M.5 2l4.5 3.5L9.5 2" stroke="#fff" stroke-width="1" fill="none"/></svg>| info@corvaneindustries.example</div>
      <div><svg viewBox="0 0 10 10"><circle cx="5" cy="5" r="4.2" fill="none" stroke="var(--red)" stroke-width="1.2"/><path d="M.8 5h8.4M5 .8c-2.4 2.6-2.4 5.8 0 8.4M5 .8c2.4 2.6 2.4 5.8 0 8.4" stroke="var(--red)" stroke-width=".8" fill="none"/></svg>| www.corvaneindustries.example</div>
      <div><svg viewBox="0 0 10 10"><path d="M5 .5a3.2 3.2 0 0 1 3.2 3.2C8.2 6 5 9.5 5 9.5S1.8 6 1.8 3.7A3.2 3.2 0 0 1 5 .5z" fill="var(--red)"/><circle cx="5" cy="3.7" r="1.1" fill="#fff"/></svg>| 1480 Millrace Road</div>
      <div>Ashford, TN 37000</div>
    </div>

    <div class="block headline cover-welcome">
      <span class="w1">Welcome</span>
      <span class="w2">to Corvane</span>
      <span class="cover-tag">INDUSTRIES, INC.</span>
    </div>
  </section>

  <!-- INSIDE SPREAD -->
  <section class="spread spread--inside">
    <svg class="art" viewBox="0 0 640 456" xmlns="http://www.w3.org/2000/svg">
      <defs>
        <linearGradient id="cutFill" x1="0" y1="0" x2="1" y2="1">
          <stop offset="0" stop-color="#6f7f8c"/><stop offset=".45" stop-color="#e9a545"/><stop offset="1" stop-color="#2e2a26"/>
        </linearGradient>
        <linearGradient id="partFill" x1="0" y1="0" x2="1" y2="1">
          <stop offset="0" stop-color="#c9ced6"/><stop offset=".6" stop-color="#9aa3ad"/><stop offset="1" stop-color="#5f6873"/>
        </linearGradient>
        <linearGradient id="paperFade2" x1="0" y1="0" x2="1" y2="0">
          <stop offset="0" stop-color="#d9dadf"/><stop offset=".12" stop-color="#f2f3f5"/><stop offset="1" stop-color="#eceef0"/>
        </linearGradient>
      </defs>
      <rect x="0" y="0" width="216" height="456" fill="var(--white)"/>
      <rect x="216" y="0" width="208" height="456" fill="url(#paperFade2)"/>
      <rect x="424" y="0" width="216" height="456" fill="var(--navy)"/>

      <!-- left panel: dark band sits above the heading -->
      <polygon points="0,66 119,0 232,0 232,124 60,34" fill="var(--navy)"/>
      <polygon points="0,0 119,0 0,66" fill="var(--red)"/>
      <polygon points="113,63 160,44 160,97" fill="var(--red)"/>

      <!-- middle panel -->
      <polygon points="232,0 407,0 407,236 232,150" fill="var(--white)"/>
      <g role="img" aria-label="Photo: laser cutter head cutting sheet steel with sparks">
        <polygon points="238,0 401,0 401,231 238,153" fill="url(#cutFill)"/>
      </g>
      <polygon points="232,145 232,205 287,176" fill="var(--navy)"/>

      <!-- right panel -->
      <polygon points="577,0 640,0 640,34" fill="var(--red)"/>
      <polygon points="442,212 620,312 620,456 442,456" fill="var(--white)"/>
      <polygon points="611,340 640,352 640,456 611,456" fill="var(--white)"/>
      <g role="img" aria-label="Photo: precision-machined aluminium block with bored holes">
        <polygon points="448,221 611,313 611,456 448,456" fill="url(#partFill)"/>
      </g>
      <polygon points="561,289 618,248 618,310" fill="var(--red)"/>
    </svg>

    <h2 class="block headline welcome-title">Welcome to</h2>
    <h3 class="block headline welcome-sub">Corvane Industries, Inc.</h3>
    <p class="block body-copy welcome-copy">When your project or process requires precise, high-quality parts or components, look no further than Corvane. We welcome the opportunity to quote your project, and with 40 years combined experience in precision manufacturing, you can rest assured that jobs placed with us will be done to your satisfaction, every time.</p>

    <h3 class="block headline about-title">About <span>us...</span></h3>
    <div class="block body-copy about-copy">
      <p>Corvane Industries, Inc. is a privately owned company with over fifty years of experience in precision manufacturing. Products manufactured include components for guided missile systems during Operation Desert Storm, machine gun barrels, close tolerance can tooling, conveyor slats and rollers, molds, various production tooling for several national industries, pump housings for the gasoline industry, aviation and automotive manufacturing, and various precision machining and grinding jobs.</p>
      <p>Currently, Corvane Industries, Inc. is working with a group of physicians to develop and patent various surgical devices for use in Orthopedic and General Vascular surgeries.</p>
    </div>

    <p class="block letter">
      <span class="greet">We at<br>Corvane Industries, <span>Inc.</span></span>
      look forward to the opportunity to<br>
      work with you and quote any projects<br>
      you might want us to look at. We take a “Quality<br>
      first” approach to all of our jobs and we have<br>
      the determination to get the job done<br>
      according to our clients’ timelines. We are<br>
      always looking for opportunities to form new<br>
      alliances and friendships with prospective<br>
      clients.
    </p>

    <div class="block signoff">
      <p class="regards">Best regards,</p>
      <div class="row"><span>Daniel R. Hollis</span><span>Mark Hollis</span></div>
      <div class="row"><span>President / Shop Manager</span><span>COO</span></div>
    </div>
    <p class="block body-copy closing">Contact us today and let us help you make your product a success!</p>

    <p class="block body-copy services-intro">We at Corvane offer a wide variety of services to meet your machining and tooling needs.</p>
    <div class="block cap-label">OUR CAPABILITIES INCLUDE -</div>
    <ul class="block cap-list">
      <li class="pair"><span>Soft cutting</span><span>Hard cutting</span></li>
      <li class="pair"><span>CNC Machining</span><span>CNC Milling</span></li>
      <li class="pair"><span>0-2 Micro-finishing</span><span>Light fabrication</span></li>
      <li>NAICS 332813, 332721 &amp; 333512</li>
      <li>Grinding- O.D./ I.D. and Surface/Rotary (Carbide, Steel, etc.)</li>
      <li>Conveyor assemblies - slats, rollers, etc.</li>
      <li>Can tooling- Trimmer Knives, Knockouts, Punch Bolts, Printer Mandrels, Cut Edges, Blank and Draw Dies, etc.</li>
      <li>Wide range of Aerospace and Automotive tooling</li>
    </ul>
  </section>

</div>
</body>
</html>
```